Banner for back of trucks

We make a product that is called "Brindo".
It attaches to the side of hay balers and automatically applies tags to bales as they are being made.
We require a simple / modern banner design that will be affixed to the back of hay trucks showing that the hay on board has been Marked by Brindo.
The banner will be 52x91cm (landscape)
The banner needs to say "Marked by Brindo" using the company logo.
It also needs the website "www.brindo.com.au" displayed.
We have attached an image of our logo, the product itself and the back of a truck it will be attached to for reference.

```html
<!DOCTYPE html>
<html lang="en">
<head>
<meta charset="utf-8">
<title>Marked by Brindo – Truck Banner</title>
<link href="https://fonts.googleapis.com/css2?family=Jost:wght@400;500;900&display=swap" rel="stylesheet">
<style>
  :root {
    --backdrop: #979797;
    --paper: #ffffff;
    --orange: #f9ad44;
    --brown: #574a3d;
    --ink: #111111;
    --product-light: #e3e2dc;
    --product-shade: #c4c3bc;
  }
  html, body {
    margin: 0;
    width: 1200px;
    height: 1200px;
    overflow: hidden;
    background: var(--backdrop);
    font-family: "Jost", "Futura", sans-serif;
  }
  .banner {
    position: absolute;
    left: 110px;
    top: 321px;
    width: 980px;
    height: 558px;
    background: var(--paper);
    overflow: hidden;
  }
  .banner-shapes {
    position: absolute;
    inset: 0;
    width: 100%;
    height: 100%;
  }
  .brand-name {
    position: absolute;
    left: 65px;
    top: 52px;
    margin: 0;
    font-weight: 400;
    font-size: 66px;
    line-height: 1;
    letter-spacing: 6px;
    color: var(--brown);
  }
  .headline {
    position: absolute;
    left: 65px;
    top: 346px;
    margin: 0;
    color: var(--ink);
  }
  .headline-main {
    display: block;
    font-weight: 900;
    font-size: 70px;
    line-height: 1;
    letter-spacing: 1px;
  }
  .headline-sub {
    display: block;
    margin-top: 12px;
    font-weight: 400;
    font-size: 44px;
    line-height: 1;
  }
  .website {
    position: absolute;
    left: 600px;
    top: 416px;
    width: 380px;
    height: 59px;
    margin: 0;
    display: flex;
    align-items: center;
    justify-content: center;
    font-weight: 400;
    font-size: 27px;
    line-height: 1;
    letter-spacing: 0.5px;
    color: var(--paper);
  }
</style>
</head>
<body>
  <section class="banner">
    <svg class="banner-shapes" viewBox="0 0 784 446" preserveAspectRatio="none">
      <defs>
        <linearGradient id="fieldPhotoTone" x1="0" y1="0" x2="1" y2="1">
          <stop offset="0" stop-color="#4f9a36"/>
          <stop offset="0.45" stop-color="#d9d8d2"/>
          <stop offset="1" stop-color="#3d7f2c"/>
        </linearGradient>
        <linearGradient id="productTone" x1="0" y1="0" x2="1" y2="1">
          <stop offset="0" stop-color="var(--product-light)"/>
          <stop offset="1" stop-color="var(--product-shade)"/>
        </linearGradient>
      </defs>

      <polygon class="orange-field" points="0,175 347,175 452,423 784,423 784,446 0,446" fill="var(--orange)"/>

      <polygon class="field-photo" role="img" aria-label="Photo of the Brindo tagging unit mounted on the side of a green hay baler"
               points="284,0 664,0 784,173 784,258 412,258" fill="url(#fieldPhotoTone)"/>

      <polygon class="corner-band" points="700,0 784,0 784,120" fill="var(--brown)"/>

      <rect class="product-photo" role="img" aria-label="Cut-out photo of the Brindo bale tagging unit"
            x="148" y="130" width="214" height="126" fill="url(#productTone)"/>

      <line class="accent-rule" x1="52" y1="223" x2="137" y2="223" stroke="var(--ink)" stroke-width="2"/>
      <line class="accent-rule" x1="220" y1="400" x2="402" y2="400" stroke="var(--ink)" stroke-width="2"/>
      <line class="accent-diagonal" x1="367" y1="263" x2="462" y2="408" stroke="var(--ink)" stroke-width="2"/>

      <polygon class="web-band" points="472,333 784,333 784,380 497,380" fill="var(--brown)"/>
    </svg>

    <p class="brand-name">Brindo</p>

    <h1 class="headline">
      <span class="headline-main">MARKED</span>
      <span class="headline-sub">by Brindo</span>
    </h1>

    <p class="website">www.brindo.com.au</p>
  </section>
</body>
</html>
```